Lumo Habitat Real estate Costa del sol

we need a website for our Company based in Costa del sol, Spain. We sell properties on the spanish coast that is called costa del sol. We are concentrating on exclusive properties and would like the webdesign to show this. In our website we want to have area descriptions of the different areas we sell our Products. We will also implement a searchable database delivered by a third part where all properties for sale in Spain are listed. When looking into the designs we would like our main page to have a overview of the coast where the different areas are shown. Have a look at brightvillarow.com or mykelsa.com to see. The webpage will be presented in 4 languages, English, spanish, Swedish and norwegian, and shall of course also be prepared for social medias. We want an easy Contemporary design but still with an exclusive feeling!
Target Market(s)
Scandinavian and North european Citizens wants to buy a property in Spain
Industry/Entity Type
Real Estate
Number of Pages Required
5+ page
Look and feel

```html
<!DOCTYPE html>
<html lang="en">
<head>
<meta charset="utf-8">
<title>Lumo Habitat – Properties on the Spanish Coast</title>
<link rel="stylesheet" href="https://fonts.googleapis.com/css2?family=Montserrat:wght@400;500;600&family=Open+Sans:wght@400;600&display=swap">
<style>
:root{
  --navy:#0b0b3b;
  --navy-soft:#2b2c5a;
  --grey-band:#e6e6e6;
  --search-band:#e9e9f2;
  --footer-bg:#efefef;
  --text:#333;
  --muted:#8a8a8a;
  --blue:#2a9fd2;
  --white:#fff;
  --line:#cfcfd6;
}
*{margin:0;padding:0;box-sizing:border-box}
html,body{width:1200px;height:2605px;overflow:hidden;background:var(--white)}
body{position:relative;font-family:"Open Sans",Arial,sans-serif;color:var(--text)}
.abs{position:absolute}
.head-font{font-family:"Montserrat",Arial,sans-serif}

/* header */
.brand{position:absolute;left:0;width:1200px;top:40px;display:flex;justify-content:center;align-items:center;gap:12px}
.brand-mark{width:20px;height:20px;background:var(--navy)}
.brand-name{font-family:"Montserrat",Arial,sans-serif;font-weight:500;font-size:30px;color:var(--navy);letter-spacing:.5px}
.lang{left:957px;top:54px;width:108px;height:29px;border:1px solid #ddd;border-radius:2px;font-size:13px;display:flex;align-items:center;gap:7px;padding-left:10px}
.flag{width:20px;height:13px;background:linear-gradient(135deg,#1f3b8c,#c8102e)}
.phone{left:898px;top:104px;font-family:"Montserrat",Arial,sans-serif;font-size:20px;font-weight:500;color:var(--navy);display:flex;align-items:center;gap:6px}

/* nav */
.nav{left:0;top:156px;width:1200px;height:54px;background:var(--navy)}
.nav-home{position:absolute;left:123px;top:0;width:68px;height:54px;background:#8b8b93;display:flex;align-items:center;justify-content:center}
.nav-item{position:absolute;top:0;height:54px;line-height:54px;color:var(--white);font-family:"Montserrat",Arial,sans-serif;font-size:18px;transform:translateX(-50%);white-space:nowrap}
.nav-sep{position:absolute;top:0;width:1px;height:54px;background:#33345e}

/* hero */
.hero{left:0;top:210px;width:1200px;height:431px;background:linear-gradient(180deg,#1d3558 0%,#4a5d78 45%,#7a6a55 75%,#3f4a35 100%)}
.hero-title{left:125px;top:200px;font-family:"Montserrat",Arial,sans-serif;font-size:35px;font-weight:500;color:var(--white);line-height:45px;letter-spacing:.5px}
.dots{left:552px;top:606px;display:flex;gap:4px}
.dots span{width:14px;height:14px;border-radius:50%;background:var(--white)}
.dots span.off{background:transparent;border:2px solid var(--white)}

/* search */
.search{left:0;top:641px;width:1200px;height:175px;background:var(--search-band)}
.field{position:absolute;height:40px;background:var(--white);border:1px solid var(--line);font-size:13px;color:#777;padding-left:16px;line-height:38px}
.field svg{position:absolute;right:12px;top:14px}
.search-btn{position:absolute;left:778px;top:85px;width:264px;height:40px;background:var(--navy);color:var(--white);font-family:"Montserrat",Arial,sans-serif;font-weight:600;font-size:16px;text-align:center;line-height:40px}

/* feature cards */
.feature{top:842px;width:306px;height:259px;border:2px solid #ddd;padding:5px}
.feature-photo{width:100%;height:247px}
.feature-caption{position:absolute;left:7px;right:7px;bottom:7px;height:105px;background:rgba(20,20,70,.85);color:var(--white);text-align:center}
.feature-caption.grey{background:rgba(110,110,110,.9)}
.feature-caption h3{font-family:"Montserrat",Arial,sans-serif;font-weight:400;font-size:18px;margin-top:11px;letter-spacing:.5px}
.feature-caption p{font-size:12px;line-height:17px;margin:14px 22px 0;color:#dcdce8}

/* about */
.about{left:139px;top:1136px;width:938px;height:354px;background:var(--navy);overflow:hidden}
.about-photo{position:absolute;left:0;top:0;width:938px;height:354px}
.about-body{position:absolute;left:507px;top:60px;width:410px;color:var(--white)}
.about-body h2{font-family:"Montserrat",Arial,sans-serif;font-weight:400;font-size:25px;letter-spacing:.5px}
.about-body p{font-size:14px;line-height:24px;margin-top:12px;color:#e4e4f0}
.btn-more{display:inline-block;margin-top:22px;width:118px;height:35px;line-height:35px;text-align:center;background:#20226a;font-family:"Montserrat",Arial,sans-serif;font-size:11px;font-weight:600;letter-spacing:.5px}

/* areas */
.areas{left:0;top:1532px;width:1200px;height:427px;background:var(--grey-band)}
.areas-notch{position:absolute;left:578px;top:0;transform:translateX(-50%)}
.section-title{position:absolute;left:0;width:1200px;top:40px;text-align:center;font-family:"Montserrat",Arial,sans-serif;font-size:22px;color:#222;letter-spacing:.5px}
.area-card{position:absolute;top:92px;width:228px;height:285px;background:var(--white)}
.area-photo{width:228px;height:151px}
.area-card h4{font-family:"Montserrat",Arial,sans-serif;font-weight:500;font-size:17px;color:var(--navy);margin:14px 0 0 22px}
.area-card p{font-size:11px;line-height:16px;color:var(--muted);margin:6px 18px 0 22px}
.area-card .more{font-size:12px;font-weight:600;color:#111;margin:5px 0 0 22px}

/* blogs */
.blogs-title{left:135px;top:2012px;font-family:"Montserrat",Arial,sans-serif;font-size:23px;color:var(--blue);letter-spacing:.5px}
.blog{top:2071px;width:290px}
.blog h5{font-weight:400;font-size:16px;color:#444}
.blog p{font-size:12px;line-height:18px;color:var(--muted);margin-top:9px}
.blog .date{font-size:13px;color:#333;margin-top:10px;padding-left:3px}

/* footer */
.footer{left:0;top:2286px;width:1200px;height:253px;background:var(--footer-bg)}
.footer-brand{position:absolute;left:122px;top:105px;display:flex;align-items:center;gap:10px}
.footer-brand .brand-mark{width:16px;height:16px}
.footer-brand .brand-name{font-size:24px}
.foot-col{position:absolute;top:42px}
.foot-col h6{font-family:"Montserrat",Arial,sans-serif;font-weight:400;font-size:16px;color:#333;letter-spacing:.3px}
.foot-col ul{list-style:none;margin-top:10px}
.foot-col li{font-size:12.5px;color:#555;line-height:24.5px}
.foot-sep{position:absolute;top:41px;width:1px;height:160px;background:#ccc}
.social{display:flex;gap:4px;margin-top:12px}
.social span{width:32px;height:32px;border:1.5px solid #666;border-radius:50%}
.copyright{left:0;top:2562px;width:1157px;text-align:center;font-size:11.5px;color:#666}
</style>
</head>
<body>

<header>
  <div class="brand"><span class="brand-mark"></span><span class="brand-name">Lumo Habitat</span></div>
  <div class="abs lang"><span class="flag" role="img" aria-label="English flag"></span>English
    <svg width="9" height="6" viewBox="0 0 9 6"><path d="M0 0h9L4.5 6z" fill="#555"/></svg></div>
  <div class="abs phone">
    <svg width="18" height="18" viewBox="0 0 24 24"><path fill="#0b0b3b" d="M6.6 10.8a15.1 15.1 0 0 0 6.6 6.6l2.2-2.2c.3-.3.7-.4 1-.2 1.1.4 2.3.6 3.6.6.6 0 1 .4 1 1V20c0 .6-.4 1-1 1A17 17 0 0 1 3 4c0-.6.4-1 1-1h3.5c.6 0 1 .4 1 1 0 1.3.2 2.5.6 3.6.1.3 0 .7-.2 1z"/></svg>
    612 4471 3085</div>
</header>

<nav class="abs nav">
  <div class="nav-home"><svg width="24" height="22" viewBox="0 0 24 22"><path fill="#fff" d="M12 1 1 11h3v10h6v-6h4v6h6V11h3z"/></svg></div>
  <span class="nav-item" style="left:269px">About Us</span>
  <span class="nav-sep" style="left:332px"></span>
  <span class="nav-item" style="left:400px">Our Service</span>
  <span class="nav-sep" style="left:462px"></span>
  <span class="nav-item" style="left:533px">Properties</span>
  <span class="nav-sep" style="left:599px"></span>
  <span class="nav-item" style="left:633px">Sell</span>
  <span class="nav-sep" style="left:666px"></span>
  <span class="nav-item" style="left:717px">Blogs</span>
  <span class="nav-sep" style="left:755px"></span>
  <span class="nav-item" style="left:834px">Life in Spain</span>
  <span class="nav-sep" style="left:912px"></span>
  <span class="nav-item" style="left:974px">Contact Us</span>
</nav>

<section class="abs hero" role="img" aria-label="Modern two-storey home lit at dusk with timber facade and front lawn"></section>
<h1 class="abs hero-title">WE SELL PROPERTIES<br>ON THE SPANISH COAST</h1>
<div class="abs dots"><span class="off"></span><span></span><span></span><span></span></div>

<section class="abs search">
  <div class="field" style="left:135px;top:35px;width:263px">Select Location<svg width="12" height="8" viewBox="0 0 12 8"><path d="M1 1l5 5 5-5" stroke="#555" stroke-width="1.6" fill="none"/></svg></div>
  <div class="field" style="left:412px;top:35px;width:260px">All Types<svg width="12" height="8" viewBox="0 0 12 8"><path d="M1 1l5 5 5-5" stroke="#555" stroke-width="1.6" fill="none"/></svg></div>
  <div class="field" style="left:691px;top:35px;width:167px">Bedroom<svg width="12" height="8" viewBox="0 0 12 8"><path d="M1 1l5 5 5-5" stroke="#555" stroke-width="1.6" fill="none"/></svg></div>
  <div class="field" style="left:872px;top:35px;width:170px">Bathroom<svg width="12" height="8" viewBox="0 0 12 8"><path d="M1 1l5 5 5-5" stroke="#555" stroke-width="1.6" fill="none"/></svg></div>
  <div class="field" style="left:135px;top:85px;width:263px">Sub TYpe<svg width="12" height="8" viewBox="0 0 12 8"><path d="M1 1l5 5 5-5" stroke="#555" stroke-width="1.6" fill="none"/></svg></div>
  <div class="field" style="left:412px;top:85px;width:172px">Min Price<svg width="12" height="8" viewBox="0 0 12 8"><path d="M1 1l5 5 5-5" stroke="#555" stroke-width="1.6" fill="none"/></svg></div>
  <div class="field" style="left:594px;top:85px;width:170px">Max Price<svg width="12" height="8" viewBox="0 0 12 8"><path d="M1 1l5 5 5-5" stroke="#555" stroke-width="1.6" fill="none"/></svg></div>
  <div class="search-btn">SEARCH</div>
</section>

<section>
  <article class="abs feature" style="left:127px">
    <div class="feature-photo" role="img" aria-label="Large white family house with garage under blue sky" style="background:linear-gradient(180deg,#7fa8d6,#c9c4bb 60%,#8a8f82)"></div>
    <div class="feature-caption"><h3>OUR PROPERTIES</h3><p>Morbi diam mauris viverra in gravida eu mattis in ante Morbi eget arcu</p></div>
  </article>
  <article class="abs feature" style="left:445px">
    <div class="feature-photo" role="img" aria-label="White Mediterranean apartment building with palm trees" style="background:linear-gradient(180deg,#2f7fd0,#e8e4dc 60%,#5f7a45)"></div>
    <div class="feature-caption grey"><h3>NEW DEVELOPMENT</h3><p>Morbi diam mauris viverra in gravida eu mattis in ante Morbi eget arcu</p></div>
  </article>
  <article class="abs feature" style="left:763px">
    <div class="feature-photo" role="img" aria-label="Whitewashed townhouses with green climbing plants" style="background:linear-gradient(180deg,#4f8fd8,#f0ede6 50%,#4d6b3c)"></div>
    <div class="feature-caption"><h3>WHY WE ARE</h3><p>Morbi diam mauris viverra in gravida eu mattis in ante Morbi eget arcu</p></div>
  </article>
</section>

<section class="abs about">
  <svg class="about-photo" viewBox="0 0 938 354" role="img" aria-label="Luxury villa with pool and garden lights at twilight">
    <defs><linearGradient id="dusk" x1="0" y1="0" x2="0" y2="1"><stop offset="0" stop-color="#5a6aa8"/><stop offset=".55" stop-color="#8a6a5a"/><stop offset="1" stop-color="#2f6a8a"/></linearGradient></defs>
    <polygon points="0,0 490,0 413,354 0,354" fill="url(#dusk)"/>
  </svg>
  <div class="about-body">
    <h2>ABOUT LUMO HABITAT</h2>
    <p>Morbi diam mauris viverra in gravida eu mattis in ante Morbi eget arcu Morbi porta libero id ullamcorpe</p>
    <p>r nonummy nibh ligula pulvinar metus eget consectetuer augue nisi quis lacus Ut ac mi quis lacus mollis aliquam Curabitur iaculis tempus eros Curabitur vel</p>
    <span class="btn-more">READ MORE</span>
  </div>
</section>

<section class="abs areas">
  <svg class="areas-notch" width="50" height="24" viewBox="0 0 50 24"><path d="M0 0h50L25 24z" fill="#fff"/></svg>
  <h2 class="section-title">DIFFERENT AREAS WE SELL</h2>
  <article class="area-card" style="left:123px">
    <div class="area-photo" role="img" aria-label="Coastal town with red roofs and turquoise sea" style="background:linear-gradient(180deg,#6fb0e0,#c9b8a0 55%,#b5643e)"></div>
    <h4>Property Area Tittle</h4><p>Morbi diam mauris viverra in gravida eu mattis in ante Morbi eget arcu Morbi porta libero ullam</p><div class="more">LEARN MORE</div>
  </article>
  <article class="area-card" style="left:363px">
    <div class="area-photo" role="img" aria-label="Historic square with fountain and church" style="background:linear-gradient(180deg,#5d93d0,#c7b79a 55%,#8a7a62)"></div>
    <h4>Property Area Tittle</h4><p>Morbi diam mauris viverra in gravida eu mattis in ante Morbi eget arcu Morbi porta libero ullam</p><div class="more">LEARN MORE</div>
  </article>
  <article class="area-card" style="left:601px">
    <div class="area-photo" role="img" aria-label="Golden domed cathedral with palm trees at sunset" style="background:linear-gradient(180deg,#d8a86a,#c98a45 50%,#5a4a3a)"></div>
    <h4>Property Area Tittle</h4><p>Morbi diam mauris viverra in gravida eu mattis in ante Morbi eget arcu Morbi porta libero ullam</p><div class="more">LEARN MORE</div>
  </article>
  <article class="area-card" style="left:841px">
    <div class="area-photo" role="img" aria-label="City plaza with fountain and towers" style="background:linear-gradient(180deg,#6f9fd4,#b8b0a2 55%,#6b7a5a)"></div>
    <h4>Property Area Tittle</h4><p>Morbi diam mauris viverra in gravida eu mattis in ante Morbi eget arcu Morbi porta libero ullam</p><div class="more">LEARN MORE</div>
  </article>
</section>

<section>
  <h2 class="abs blogs-title">LATEST BLOGS</h2>
  <article class="abs blog" style="left:135px"><h5>Donec dictum lectus non</h5><p>Morbi diam mauris viverra in gravida eu mattis in ante Morbi eget arcu Morbi porta libero id ullamcorper nonummy nibh ligu</p><div class="date">Posted 2 days ago</div></article>
  <article class="abs blog" style="left:453px"><h5>Nullam enim leo egesta</h5><p>Morbi diam mauris viverra in gravida eu mattis in ante Morbi eget arcu Morbi porta libero id ullamcorper nonummy nibh ligu</p><div class="date">Posted 2 days ago</div></article>
  <article class="abs blog" style="left:775px"><h5>Pellentesque rutrum</h5><p>Morbi diam mauris viverra in gravida eu mattis in ante Morbi eget arcu Morbi porta libero id ullamcorper nonummy nibh ligu</p><div class="date">Posted 2 days ago</div></article>
</section>

<footer class="abs footer">
  <div class="footer-brand"><span class="brand-mark"></span><span class="brand-name">Lumo Habitat</span></div>
  <div class="foot-col" style="left:372px"><h6>COMPANY</h6><ul><li>Home</li><li>About Us</li><li>What We Do</li><li>How We Work</li></ul></div>
  <span class="foot-sep" style="left:498px"></span>
  <div class="foot-col" style="left:552px"><h6>RESOURCERS</h6><ul><li>Our Services</li><li>Support</li><li>FAQ</li><li>Blogs</li></ul></div>
  <span class="foot-sep" style="left:700px"></span>
  <div class="foot-col" style="left:729px"><h6>CONTACT INFO</h6><ul><li>18 Calle Brisa, Nerja 29780</li><li>952 301 774</li><li>900 412 388</li><li>LIC 480193B</li></ul></div>
  <span class="foot-sep" style="left:898px"></span>
  <div class="foot-col" style="left:931px"><h6>FOLLOW US</h6><div class="social"><span></span><span></span><span></span><span></span></div></div>
</footer>
<p class="abs copyright">© 2016 Company Name &nbsp;All right reserved &nbsp;Term of Use</p>

</body>
</html>
```